Business Card Design Project

use new logo uploaded.

any 3d or shadowing is nice.

white or grey background. metallic brushed silver maybe

horizontal landscape layout

Target Market(s)

dermatologist, plastic surgeons, medpas

Industry/Entity Type

Landscape

Font styles to use
Sans Serif
Other font styles liked:
• use logo font

Requirements
Must have
• horizontal landscape layout
Nice to have
• try font in logo or something like arial

```html
<!DOCTYPE html>
<html lang="en">
<head>
<meta charset="utf-8">
<title>Lumina Skin Lasers – Business Card</title>
<link rel="stylesheet" href="https://fonts.googleapis.com/css2?family=Josefin+Sans:wght@400;600&display=swap">
<style>
  :root {
    --backdrop: #e6e6e8;
    --card-white: #f7f7f8;
    --plum: #7e3f86;
    --plum-light: #9a5aa1;
    --sky: #5fc3e4;
    --sky-deep: #2f8fc0;
    --ink-grey: #6b6b70;
    --text-light: #ffffff;
  }
  * { margin: 0; padding: 0; box-sizing: border-box; }
  html, body {
    width: 1200px; height: 675px; overflow: hidden;
    background: var(--backdrop);
    font-family: "Josefin Sans", Arial, sans-serif;
  }
  .card {
    position: absolute; left: 180px; top: 97px;
    width: 840px; height: 480px;
    background: var(--card-white);
    overflow: hidden;
  }
  .card-shapes { position: absolute; inset: 0; }
  .brand-block {
    position: absolute; left: 70px; top: 190px;
    display: flex; align-items: center; gap: 18px;
  }
  .brand-dot {
    width: 34px; height: 34px; border-radius: 50%;
    background: var(--plum);
  }
  .brand-name {
    font-weight: 600; font-size: 30px; letter-spacing: 3px;
    color: var(--ink-grey); text-transform: uppercase; line-height: 1.25;
  }
  .contact-block {
    position: absolute; left: 470px; top: 90px;
    color: var(--text-light);
  }
  .contact-company {
    font-weight: 600; font-size: 27px; letter-spacing: 2.5px;
    text-transform: uppercase; margin-bottom: 22px;
  }
  .contact-line {
    font-size: 15px; letter-spacing: 1.5px; text-transform: uppercase;
    line-height: 1.55; padding-left: 46px;
  }
  .contact-gap { height: 24px; }
  .contact-email { text-transform: none; }
  .label { display: inline-block; width: 62px; text-transform: uppercase; }
</style>
</head>
<body>
  <div class="card">
    <svg class="card-shapes" width="840" height="480" viewBox="0 0 840 480" aria-hidden="true">
      <defs>
        <linearGradient id="plumFill" x1="0" y1="1" x2="1" y2="0">
          <stop offset="0" stop-color="var(--plum-light)"/>
          <stop offset="1" stop-color="var(--plum)"/>
        </linearGradient>
      </defs>
      <polygon points="440,0 840,0 840,480 330,480" fill="url(#plumFill)"/>
      <line x1="430" y1="0" x2="320" y2="480" stroke="var(--sky)" stroke-width="3"/>
      <line x1="436" y1="0" x2="326" y2="480" stroke="var(--sky-deep)" stroke-width="2"/>
    </svg>

    <div class="brand-block">
      <span class="brand-dot"></span>
      <div class="brand-name">Lumina<br>Skin Lasers</div>
    </div>

    <div class="contact-block">
      <div class="contact-company">Lumina Skin Lasers</div>
      <div class="contact-line">2150 W Birch Ln.</div>
      <div class="contact-line">Lakewood CO 80226</div>
      <div class="contact-gap"></div>
      <div class="contact-line"><span class="label">PH -</span>(555) 214-3870</div>
      <div class="contact-line"><span class="label">Fax -</span>(555) 214-3871</div>
      <div class="contact-gap"></div>
      <div class="contact-line contact-email"><span class="label">E-mail</span>info@luminaskinlasers.com</div>
    </div>
  </div>
</body>
</html>
```